Morvela Aesthetic Doctor

I require an elegant, luxurious looking business card for my aesthetic business. I am a doctor and that will set me aside from competitors. I am planning to provide home and spa based treatments to clients with high expectations. I have attached my logo.

```html
<!DOCTYPE html>
<html lang="en">
<head>
<meta charset="utf-8">
<title>Morvela Aesthetic Doctor – Business Card</title>
<link href="https://fonts.googleapis.com/css2?family=Cabin:wght@400;500&display=swap" rel="stylesheet">
<style>
  :root {
    --backdrop: #92a5a3;
    --navy: #0d1726;
    --band: #f1f1f1;
    --cyan: #4cc6ea;
    --white: #ffffff;
    --icon-disc: #eeeeee;
  }
  * { margin: 0; padding: 0; box-sizing: border-box; }
  html, body { width: 1200px; height: 857px; overflow: hidden; }
  body {
    background: var(--backdrop);
    font-family: "Cabin", sans-serif;
    position: relative;
  }
  .card {
    position: absolute;
    top: 131px;
    width: 363px;
    height: 606px;
    background: var(--navy);
    overflow: hidden;
  }
  .card--front { left: 190px; }
  .card--back { left: 653px; }

  .wordmark {
    position: absolute;
    display: flex;
    align-items: center;
    gap: 10px;
    color: var(--cyan);
    font-weight: 400;
  }
  .wordmark__disc {
    flex: none;
    border-radius: 50%;
    border: 2px solid var(--cyan);
  }
  .wordmark__name { line-height: 1.05; letter-spacing: 0.06em; text-transform: uppercase; }

  .card--front .wordmark { left: 78px; top: 276px; }
  .card--front .wordmark__disc { width: 52px; height: 52px; }
  .card--front .wordmark__name { font-size: 19px; }

  .tagline {
    position: absolute;
    left: 0; right: 0; top: 524px;
    text-align: center;
    color: var(--cyan);
    font-size: 13px;
  }

  .band {
    position: absolute;
    left: 0; top: 0; right: 0;
    height: 102px;
    background: var(--band);
  }
  .card--back .wordmark { left: 84px; top: 66px; }
  .card--back .wordmark__disc { width: 56px; height: 56px; background: var(--band); }
  .card--back .wordmark__name { font-size: 17px; }

  .rule {
    position: absolute;
    left: 85px;
    width: 194px;
    height: 2px;
    background: var(--cyan);
  }
  .rule--top { top: 162px; }
  .rule--bottom { top: 468px; }

  .doctor-name {
    position: absolute;
    left: 0; right: 0; top: 181px;
    text-align: center;
    color: var(--white);
    font-size: 13px;
  }
  .credentials {
    position: absolute;
    left: 0; right: 0; top: 216px;
    text-align: center;
    color: var(--cyan);
    font-size: 8.5px;
    line-height: 16px;
  }

  .contacts {
    position: absolute;
    left: 87px; top: 297px;
    list-style: none;
  }
  .contact {
    display: flex;
    align-items: center;
    gap: 21px;
    height: 36px;
    margin-bottom: 9px;
    color: var(--white);
    font-size: 14.5px;
  }
  .contact__icon {
    width: 36px; height: 36px;
    border-radius: 50%;
    background: var(--icon-disc);
    display: flex; align-items: center; justify-content: center;
  }
  .contact__icon svg { width: 20px; height: 20px; }

  .services {
    position: absolute;
    left: 0; right: 0; top: 499px;
    text-align: center;
    color: var(--cyan);
    font-size: 11px;
    line-height: 13.5px;
  }
</style>
</head>
<body>
  <section class="card card--front">
    <div class="wordmark">
      <span class="wordmark__disc"></span>
      <span class="wordmark__name">Morvela<br>Aesthetic Doctor</span>
    </div>
    <p class="tagline">Home and Spa Based Treatments</p>
  </section>

  <section class="card card--back">
    <div class="band"></div>
    <div class="wordmark">
      <span class="wordmark__disc"></span>
      <span class="wordmark__name">Morvela<br>Aesthetic Doctor</span>
    </div>

    <div class="rule rule--top"></div>
    <p class="doctor-name">Dr Elin Varga</p>
    <p class="credentials">MRCPCH MD Australasian Diploma<br>of Aesthetic Medicine</p>

    <ul class="contacts">
      <li class="contact">
        <span class="contact__icon">
          <svg viewBox="0 0 24 24"><path fill="#4cc6ea" d="M6.6 10.8a15.1 15.1 0 0 0 6.6 6.6l2.2-2.2a1 1 0 0 1 1-.25 11.4 11.4 0 0 0 3.6.57 1 1 0 0 1 1 1V20a1 1 0 0 1-1 1A17 17 0 0 1 3 4a1 1 0 0 1 1-1h3.5a1 1 0 0 1 1 1c0 1.25.2 2.45.57 3.6a1 1 0 0 1-.25 1z"/></svg>
        </span>
        <span>0800 555 014</span>
      </li>
      <li class="contact">
        <span class="contact__icon">
          <svg viewBox="0 0 24 24"><rect x="2" y="5" width="20" height="14" rx="1.5" fill="#4cc6ea"/><path d="M3 6.5l9 6.5 9-6.5M3 17.5l6.5-5.5M21 17.5l-6.5-5.5" fill="none" stroke="#ffffff" stroke-width="1"/></svg>
        </span>
        <span>elin@morvela.co.nz</span>
      </li>
      <li class="contact">
        <span class="contact__icon">
          <svg viewBox="0 0 24 24" fill="none" stroke="#4cc6ea" stroke-width="1.3"><circle cx="12" cy="12" r="9"/><ellipse cx="12" cy="12" rx="4" ry="9"/><path d="M3 12h18M4.5 7.5h15M4.5 16.5h15M12 3v18"/></svg>
        </span>
        <span>www.morvela.co.nz</span>
      </li>
    </ul>

    <div class="rule rule--bottom"></div>
    <p class="services">Dermal injectables - Plasma facials - Microneedling<br>Skin boosters - Excessive sweating<br>Home and Spa Based Treatments</p>
  </section>
</body>
</html>
```